Wordpress website update with basic ecomm features

We need an update to our existing website
www.quillharbour.com.au that can be easily updated, enhances our logo and can take payments online and a basic text logo suite for 3 products. Website would reflect confidence and give clients confidence in the outcomes we will provide for them. must be easy to use, crisp, fresh, clean and dynamic.

Target Market(s)

entrepreneurs, professionals, small business owners, corporate organisations, universities

Industry/Entity Type

Online

Coding

Coded - Design and coding required

Number of Pages Required

5+ page

Font styles to use
Sans Serif

Requirements
Must have
• be easy to navigate, look professional, please see brief doc
Nice to have
• please see briefing doc
Should not have
• please see briefing doc

```html
<!DOCTYPE html>
<html lang="en">
<head>
<meta charset="utf-8">
<title>Quill Harbour</title>
<link href="https://fonts.googleapis.com/css2?family=Open+Sans:wght@300;400;600;700&family=Roboto:wght@500;700&display=swap" rel="stylesheet">
<style>
:root{
  --blue:#1f5fb5;
  --blue-deep:#24409f;
  --navy:#17325f;
  --ink:#333;
  --muted:#666;
  --light:#f3f3f3;
  --line:#1f5fb5;
  --dark:#2b2b2b;
  --darker:#1d1d1d;
  --white:#fff;
}
*{box-sizing:border-box;margin:0;padding:0}
html,body{width:1200px;height:3742px;overflow:hidden}
body{font-family:"Open Sans",Arial,sans-serif;color:var(--ink);background:var(--white);position:relative;font-size:13px;line-height:1.55}
.abs{position:absolute}
.wrap{position:absolute;left:172px;width:856px}
h2.section-title{font-weight:300;font-size:40px;color:#333;text-align:center;line-height:1.2}
.section-sub{text-align:center;font-size:13px;color:#444;margin-top:8px}
.rule{width:120px;height:2px;background:var(--line);margin:12px auto 0}
h3.col-title{font-family:"Roboto",Arial,sans-serif;font-weight:700;font-size:22px;color:#222}
h3.col-title::after{content:"";display:block;width:48px;height:2px;background:var(--line);margin-top:6px}
.photo{background:linear-gradient(135deg,#5d6a7a,#2f3a48)}
.btn{display:inline-block;background:var(--blue-deep);color:#fff;font-weight:700;font-size:11px;text-align:center;letter-spacing:.5px}

/* top */
.topbar{top:0;left:0;width:1200px;height:35px;background:var(--blue);color:#fff;font-size:11px}
.topbar .contact{position:absolute;right:185px;top:10px;display:flex;gap:28px}
.topbar .social{position:absolute;right:76px;top:11px;display:flex;gap:9px}
.topbar .social span{width:12px;height:12px;border:1.5px solid #fff;border-radius:2px}
.hero{top:35px;left:0;width:1200px;height:539px;background:linear-gradient(120deg,#3f5166 0%,#6b7a88 40%,#2d3b4b 100%)}
.navbar{top:35px;left:0;width:1200px;height:65px;background:rgba(20,24,30,.85)}
.logo{top:0;left:162px;width:188px;height:100px;background:#fff;display:flex;align-items:center;justify-content:center}
.logo span{font-family:"Roboto",Arial,sans-serif;font-weight:700;font-size:22px;color:var(--navy)}
.nav{top:58px;left:448px;display:flex;gap:18px;font-size:11px;color:#fff;font-weight:600}
.nav .active{color:#6fa6ff}
.search{top:51px;left:986px;width:34px;height:30px;background:var(--blue)}
.caption{top:444px;left:392px;width:486px;height:130px;background:rgba(15,18,24,.88);color:#fff;font-weight:600;font-size:16px;line-height:1.55;padding:36px 24px 0}
.caption::before{content:"";position:absolute;left:24px;top:20px;width:48px;height:3px;background:var(--blue)}

/* welcome */
.welcome{top:574px;left:0;width:1200px;height:616px}
.welcome .title{position:absolute;top:52px;width:1200px}
.about{top:224px;left:172px;width:417px}
.about .photo{height:162px;margin-top:18px}
.about p{font-size:11.5px;color:#555;margin-top:10px;line-height:1.6}
.about .btn{width:95px;height:32px;line-height:32px;margin-top:16px}
.why{top:224px;left:611px;width:417px}
.why p{font-size:11.5px;color:#555;margin-top:16px;line-height:1.6}
.why ul{list-style:none;margin-top:10px}
.why li{font-size:11.5px;color:#444;padding-left:22px;position:relative;line-height:1.55;margin-bottom:5px}
.why li::before{content:"";position:absolute;left:0;top:3px;width:12px;height:12px;background:var(--blue);border-radius:2px}
.why li::after{content:"";position:absolute;left:3px;top:5px;width:5px;height:3px;border-left:2px solid #fff;border-bottom:2px solid #fff;transform:rotate(-45deg)}

/* offer */
.offer{top:1190px;left:0;width:1200px;height:487px;background:var(--light)}
.offer .title{position:absolute;top:34px;width:1200px}
.arrows{display:flex;gap:4px}
.arrows span{width:20px;height:20px;background:var(--blue-deep);position:relative}
.arrows span::after{content:"";position:absolute;left:7px;top:7px;width:5px;height:5px;border-top:2px solid #fff;border-right:2px solid #fff}
.arrows .prev::after{transform:rotate(-135deg);left:8px}
.arrows .next::after{transform:rotate(45deg);left:5px}
.offer .arrows{position:absolute;top:116px;left:984px}
.card{position:absolute;top:157px;width:270px}
.card .photo{height:138px}
.card h4{font-family:"Roboto",Arial,sans-serif;font-weight:500;font-size:15px;color:#222;margin-top:10px;line-height:1.3}
.card p{font-size:11px;color:#666;margin-top:6px;line-height:1.55}
.more{font-size:10.5px;font-weight:700;color:var(--blue-deep);margin-top:6px}

/* faq */
.faq-band{top:1677px;left:0;width:1200px;height:456px;background:#f7f7f7}
.faq{top:1722px;left:172px;width:417px}
.acc{margin-top:18px}
.acc .item{height:40px;background:var(--blue);color:#fff;font-size:12px;padding:0 14px;display:flex;align-items:center;justify-content:space-between;margin-bottom:10px}
.acc .item i{width:18px;height:18px;border:1.5px solid #fff;border-radius:50%;position:relative}
.acc .item i::before,.acc .item.plus i::after{content:"";position:absolute;background:#fff;left:3.5px;top:7.2px;width:8px;height:1.5px}
.acc .item.plus i::after{transform:rotate(90deg)}
.acc .item.open{margin-bottom:0}
.acc .body{background:#fff;border:1px solid #ddd;border-top:0;padding:16px 14px;font-size:11.5px;color:#555;line-height:1.6;margin-bottom:14px;height:112px}
.testi{top:1722px;left:611px;width:417px}
.quote{display:flex;gap:14px;margin-top:22px}
.quote .photo{width:122px;height:124px;flex:none;background:linear-gradient(135deg,#b9c0c8,#6c7683)}
.quote p{font-size:11px;color:#555;line-height:1.6}
.quote .name{font-size:11px;color:#333;margin-top:8px}
.quote .role{font-size:10px;color:var(--blue);font-style:italic}
.quote .mark{font-family:Georgia,serif;font-size:28px;color:#bbb;line-height:.6;height:16px}
.sep{height:1px;background:#ddd;margin-top:14px;margin-left:136px}
.testi .arrows{position:absolute;left:370px;top:336px}

/* events */
.events{top:2133px;left:0;width:1200px;height:455px}
.events .title{position:absolute;top:44px;width:1200px}
.events .arrows{position:absolute;top:172px;left:984px}
.event{position:absolute;top:202px;width:199px;height:213px;background:#fff;border:1px solid #e3e3e3}
.event .photo{height:80px}
.event h4{font-size:12.5px;font-weight:600;color:#222;padding:8px 8px 0;line-height:1.35}
.event .meta{font-size:9.5px;color:#777;padding:6px 8px 0;display:flex;gap:16px}
.event .meta b{display:inline-block;width:7px;height:7px;background:var(--blue);border-radius:50%;margin-right:4px}
.event p{font-size:10.5px;color:#666;padding:5px 8px 0;line-height:1.5}

/* contact form */
.touch{top:2588px;left:0;width:1200px;height:451px;background:linear-gradient(135deg,#2a48b3,#2440a4 60%,#2c4dba)}
.touch h2{font-weight:300;font-size:40px;color:#fff;text-align:center;margin-top:48px;line-height:1.2}
.touch .sub{font-size:12.5px;color:#e6ebff;text-align:center;margin-top:6px}
.field{position:absolute;width:270px;height:35px;background:rgba(255,255,255,.22);color:#e8ecff;font-size:11px;padding:0 12px;display:flex;align-items:center;justify-content:space-between}
.field.sel::after{content:"";width:5px;height:5px;border-right:1.5px solid #fff;border-bottom:1.5px solid #fff;transform:rotate(45deg)}
.touch .btn{position:absolute;left:524px;top:361px;width:150px;height:38px;line-height:38px;background:#1a2440}

/* gallery and partners */
.gallery{top:3100px;left:172px;width:417px}
.grid{position:absolute;top:64px;left:0;display:grid;grid-template-columns:repeat(4,95px);gap:10px 11px}
.grid div{height:85px}
.gallery .btn{position:absolute;left:160px;top:268px;width:97px;height:25px;line-height:25px;font-size:10px}
.partners{top:3100px;left:611px;width:417px}
.pbox{position:absolute;top:64px;width:195px;height:87px;border:1px solid #ddd;display:flex;align-items:center;justify-content:center;font-family:"Roboto",Arial,sans-serif;font-weight:500;font-size:18px;color:#333}
.ptext{position:absolute;top:162px;width:195px;text-align:center;font-size:11px;color:#555;line-height:1.5}
.ptext span{display:block;margin-top:8px}

/* footer */
.footer{top:3451px;left:0;width:1200px;height:242px;background:var(--dark);color:#ddd}
.fcol{position:absolute;top:34px}
.fcol h5{font-family:"Roboto",Arial,sans-serif;font-weight:700;font-size:17px;color:#fff}
.fcol h5::after{content:"";display:block;width:40px;height:2px;background:var(--blue);margin-top:5px}
.fcol .row{font-size:11px;color:#ddd;margin-top:12px;padding-left:22px;position:relative;line-height:1.5}
.fcol .row::before{content:"";position:absolute;left:2px;top:4px;width:8px;height:8px;background:#fff;border-radius:50%}
.links{display:grid;grid-template-columns:110px 90px;margin-top:16px;font-size:11px;line-height:1.5}
.links span::before{content:"";display:inline-block;width:5px;height:5px;background:#fff;border-radius:50%;margin-right:9px;vertical-align:middle}
.nl p{font-size:11px;margin-top:14px;line-height:1.5;width:190px}
.nl .input{width:200px;height:28px;background:#444;margin-top:10px;font-size:10px;color:#bbb;padding:7px 10px}
.nl .btn{margin:10px 0 0 126px;width:74px;height:24px;line-height:24px;font-size:10px;background:var(--blue)}
.sq{display:flex;gap:8px;margin-top:18px}
.sq span{width:30px;height:30px;background:var(--blue)}
.talk{margin-top:26px;width:168px;height:38px;line-height:38px;background:var(--blue);font-size:11.5px}
.bottom{top:3693px;left:0;width:1200px;height:49px;background:var(--darker);color:#ccc;font-size:11px}
.bottom p{position:absolute;left:200px;top:16px}
.totop{position:absolute;left:986px;top:12px;width:32px;height:32px;background:var(--blue-deep)}
.totop::after{content:"";position:absolute;left:12px;top:14px;width:7px;height:7px;border-top:2px solid #fff;border-left:2px solid #fff;transform:rotate(45deg)}
</style>
</head>
<body>

<div class="abs topbar">
  <div class="contact"><span>&#9990; 111-555-0148</span><span>&#9993; info@quillharbour.com.au</span></div>
  <div class="social"><span></span><span></span><span></span></div>
</div>

<div class="abs hero photo" role="img" aria-label="Business team in a meeting around a table"></div>
<div class="abs navbar"></div>
<div class="abs logo"><span>QUILL HARBOUR</span></div>
<nav class="abs nav">
  <span class="active">HOME</span><span>ABOUT US</span><span>SERVICES</span><span>TESTIMONIAL</span><span>GALLERY</span><span>FAQ</span><span>PARTNER</span><span>CONTACT US</span>
</nav>
<div class="abs search">
  <svg width="34" height="30" viewBox="0 0 34 30"><circle cx="16" cy="14" r="6" fill="none" stroke="#fff" stroke-width="2"/><line x1="20.5" y1="18.5" x2="24" y2="22" stroke="#fff" stroke-width="2.2"/></svg>
</div>
<div class="abs caption">Quill Harbour is focused on individuals with an entrepreneurial mindset and business builders with an appreciation for the entrepreneurial journey</div>

<section class="abs welcome">
  <div class="title">
    <h2 class="section-title">Welcome to Quill Harbour</h2>
    <p class="section-sub">The Experienced Economy Shared Learning &amp; Opportunities</p>
    <div class="rule"></div>
  </div>
  <div class="abs about">
    <h3 class="col-title">About Us</h3>
    <div class="photo" role="img" aria-label="Group of people posing at an event"></div>
    <p>Quill Harbour builds and develops validation and innovation programs, communities and data to improve the overall success rate of entrepreneurial and early-stage ventures. Our aim is to build a flourishing innovation and collaboration eco-system that validates people, business &amp; society.</p>
    <span class="btn">READ MORE</span>
  </div>
  <div class="abs why">
    <h3 class="col-title">Why Choose Us</h3>
    <p>Quill Harbour is focused on individuals with an entrepreneurial mindset and business builders with an appreciation for the entrepreneurial journey.</p>
    <ul>
      <li>Best practice business education</li>
      <li>Expert facilitation that applies learning real time to ventures and opportunities</li>
      <li>Real collaboration in an environment of trust, from day one</li>
      <li>Venture, personal &amp; social outcomes</li>
      <li>Shared resourcing</li>
      <li>Powerful networks</li>
      <li>Investment &amp; industry partnerships</li>
      <li>Informal and formal meet-ups</li>
      <li>Coaching to ensure focus and continued venture progress</li>
      <li>Community, not simply network, of like-minded individuals</li>
    </ul>
  </div>
</section>

<section class="abs offer">
  <div class="title">
    <h2 class="section-title">What We Offer</h2>
    <p class="section-sub">The Experienced Economy Shared Learning &amp; Opportunities</p>
    <div class="rule"></div>
  </div>
  <div class="arrows"><span class="prev"></span><span class="next"></span></div>
  <div class="card" style="left:172px">
    <div class="photo" role="img" aria-label="Presenter at a whiteboard workshop"></div>
    <h4>Validation &amp; Business Innovation Programs</h4>
    <p>Hands-on programs that test ideas early, shape a clear plan and guide founders through each stage of growth with care.</p>
    <div class="more">Read More &#9656;</div>
  </div>
  <div class="card" style="left:467px">
    <div class="photo" role="img" aria-label="Crowded community networking room"></div>
    <h4>Validation &amp; Innovation Communities</h4>
    <p>Peer groups where founders share lessons, open doors and test new ventures together in a setting built on trust.</p>
    <div class="more">Read More &#9656;</div>
  </div>
  <div class="card" style="left:758px">
    <div class="photo" role="img" aria-label="Colourful 3D bar chart graphic" style="background:linear-gradient(135deg,#dfe8f5,#4f86d6)"></div>
    <h4>Entrepreneur &amp; Innovation Data Analytics &amp; Insights</h4>
    <p>Clear data on venture results that helps founders, partners and investors make sound choices with real confidence.</p>
    <div class="more">Read More &#9656;</div>
  </div>
</section>

<div class="abs faq-band"></div>
<section class="abs faq">
  <h3 class="col-title">FAQ</h3>
  <div class="acc">
    <div class="item open"><span>How do I join a validation program?</span><i></i></div>
    <div class="body">Apply online through our programs page. A member of our team will call you within a few days to talk through your venture, your goals and the program that best suits your stage of business right now.</div>
    <div class="item plus"><span>Who are the programs designed for?</span><i></i></div>
    <div class="item plus"><span>Can I attend community events first?</span><i></i></div>
    <div class="item plus"><span>How are payments for programs made?</span><i></i></div>
  </div>
</section>
<section class="abs testi">
  <h3 class="col-title">TESTIMONIALS</h3>
  <div class="quote">
    <div class="photo" role="img" aria-label="Portrait of a smiling businessman"></div>
    <div>
      <div class="mark">&ldquo;</div>
      <p>The program gave our team a clear plan and real focus. Within months we had tested our idea, found early clients and grown with confidence.</p>
      <div class="name">Dana Holt</div>
      <div class="role">BDM</div>
    </div>
  </div>
  <div class="sep"></div>
  <div class="quote" style="margin-top:14px">
    <div class="photo" role="img" aria-label="Portrait of a smiling businesswoman"></div>
    <div>
      <div class="mark">&ldquo;</div>
      <p>A supportive group of founders and great coaching. I left every session with practical next steps and new contacts who truly helped my business.</p>
      <div class="name">Mira Lane</div>
      <div class="role">CEO</div>
    </div>
  </div>
  <div class="arrows"><span class="prev"></span><span class="next"></span></div>
</section>

<section class="abs events">
  <div class="title">
    <h2 class="section-title">Our Upcoming Events</h2>
    <p class="section-sub">Join founders and mentors at our next sessions across Australia</p>
    <div class="rule"></div>
  </div>
  <div class="arrows"><span class="prev"></span><span class="next"></span></div>
  <div class="event" style="left:170px">
    <div class="photo" role="img" aria-label="Speaker addressing an audience"></div>
    <h4>Founder breakfast and pitch practice</h4>
    <div class="meta"><span><b></b>Melbourne</span><span><b></b>12th Nov 2016</span></div>
    <p>Pitch your idea to peers and get useful feedback over coffee</p>
  </div>
  <div class="event" style="left:392px">
    <div class="photo" role="img" aria-label="Mentors meeting at a desk"></div>
    <h4>Mentor evening for early ventures</h4>
    <div class="meta"><span><b></b>Sydney</span><span><b></b>8th Nov 2016</span></div>
    <p>Meet experienced mentors and map your next growth steps</p>
  </div>
  <div class="event" style="left:611px">
    <div class="photo" role="img" aria-label="Large crowd at a conference"></div>
    <h4>Innovation forum and panel session</h4>
    <div class="meta"><span><b></b>Melbourne</span><span><b></b>8th Nov 2016</span></div>
    <p>Hear founders share lessons on testing and scaling ideas</p>
  </div>
  <div class="event" style="left:831px">
    <div class="photo" role="img" aria-label="Workshop group at tables"></div>
    <h4>Data and insights workshop</h4>
    <div class="meta"><span><b></b>Hobart</span><span><b></b>8th Nov 2016</span></div>
    <p>Learn to read venture data and make sound choices</p>
  </div>
</section>

<section class="abs touch">
  <h2>Get In Touch!</h2>
  <p class="sub">Tell us about your venture and our team will be in touch to discuss the right program for you</p>
  <div class="field" style="left:172px;top:189px">Name</div>
  <div class="field" style="left:465px;top:189px">Email</div>
  <div class="field" style="left:758px;top:189px">Phone</div>
  <div class="field" style="left:172px;top:239px">Location / State</div>
  <div class="field sel" style="left:465px;top:239px">Do you have a current business</div>
  <div class="field sel" style="left:758px;top:239px">Do you have a business opportunity or idea</div>
  <div class="field sel" style="left:172px;top:289px">No. of people in the business</div>
  <div class="field sel" style="left:465px;top:289px">Have you started a business before</div>
  <div class="field sel" style="left:758px;top:289px">Business sector</div>
  <span class="btn">SUBMIT</span>
</section>

<section class="abs gallery">
  <h3 class="col-title">Our Gallery</h3>
  <div class="grid">
    <div class="photo" role="img" aria-label="Event photo"></div>
    <div class="photo" role="img" aria-label="Event photo"></div>
    <div class="photo" role="img" aria-label="Video thumbnail of a talk"></div>
    <div class="photo" role="img" aria-label="Event photo"></div>
    <div class="photo" role="img" aria-label="Video thumbnail of a speaker"></div>
    <div class="photo" role="img" aria-label="Event photo"></div>
    <div class="photo" role="img" aria-label="Event photo"></div>
    <div class="photo" role="img" aria-label="Event photo"></div>
  </div>
  <span class="btn">VIEW ALL</span>
</section>
<section class="abs partners">
  <h3 class="col-title">Our Partners</h3>
  <div class="pbox" style="left:0">Startway</div>
  <div class="pbox" style="left:220px">Reef Pool</div>
  <div class="ptext" style="left:0">The Future of Business<span>Business Validation &amp; Innovation Program</span></div>
  <div class="ptext" style="left:220px">The Power of Collaboration<span>Business Improvement &amp; Commercialisation Community</span></div>
</section>

<footer class="abs footer">
  <div class="fcol" style="left:172px">
    <h5>Contact Us</h5>
    <div class="row">12/40 Harbour Crest Road<br>Marlow QLD, Australia</div>
    <div class="row">111-555-0148</div>
    <div class="row">info@quillharbour.com.au</div>
  </div>
  <div class="fcol" style="left:391px">
    <h5>Links</h5>
    <div class="links">
      <span>Home</span><span>Media</span>
      <span>About Us</span><span>Our Guest</span>
      <span>Reports</span><span>Reports</span>
      <span>Gallery</span><span>FAQ</span>
      <span>Stats</span><span>Events</span>
    </div>
  </div>
  <div class="fcol nl" style="left:611px">
    <h5>Newsletter</h5>
    <p>Subscribe to our newsletter for latest updates</p>
    <div class="input">Email...</div>
    <span class="btn">SUBMIT</span>
  </div>
  <div class="fcol" style="left:831px">
    <h5>Connect With Us</h5>
    <div class="sq"><span></span><span></span><span></span><span></span></div>
    <span class="btn talk">BOOK US FOR A TALK</span>
  </div>
</footer>
<div class="abs bottom">
  <p>&copy;Copyright information here</p>
  <span class="totop"></span>
</div>

</body>
</html>
```